Velnor Group: Business Card for a high end technology company

We need a cool new design for our business cards using our cloud logo. We are a technology consulting business. We pride ourselves on be the best of the best. We mainly focus on cloud solutions and managed services. We need a business card that sets us apart from the other technology companies in the area and allows us to stand out.

Target Market(s)

Technology departments, CIO, CEOs, and Information Technology Staff.

Industry/Entity Type

Information Technology

Contact Information for Business Card

Must have the logo and our name.
Must have employee name, email address, office phone, cell phone and website.
Need to have all info on one side a cool design on backside.

Font styles to use
Serif
Sans Serif

Requirements
Must have
• Must have the logo and our name.
• Must have employee name, email address, office phone, cell phone and website.
• Need to have all info on one side a cool design on back side.
• Must be a crisp clean design, not too busy or confusing.

```html
<!DOCTYPE html>
<html lang="en">
<head>
<meta charset="utf-8">
<title>Velnor Group – Business Card</title>
<link rel="stylesheet" href="https://fonts.googleapis.com/css2?family=Open+Sans:wght@400;600&display=swap">
<style>
  :root {
    --page-bg: #3a3230;
    --card-black: #0e0f11;
    --card-pattern-top: #15202a;
    --card-pattern-bottom: #0c0f13;
    --brand-blue: #2fa3f2;
    --text-white: #f2f4f6;
    --text-soft: #d6dbe0;
    --divider: #8a9199;
  }
  * { margin: 0; padding: 0; box-sizing: border-box; }
  html, body { width: 1200px; height: 814px; overflow: hidden; }
  body {
    background: var(--page-bg);
    font-family: "Open Sans", Arial, sans-serif;
    position: relative;
  }
  .card {
    position: absolute;
    top: 258px;
    width: 520px;
    height: 297px;
    border-radius: 4px;
    box-shadow: 0 12px 30px rgba(0,0,0,0.45);
    overflow: hidden;
  }
  .card-front { left: 50px; background: var(--card-black); }
  .card-back { left: 630px; background: var(--card-black); }

  .front-brand {
    position: absolute;
    top: 108px; left: 0; right: 0;
    display: flex; align-items: center; justify-content: center; gap: 14px;
  }
  .brand-dot {
    width: 34px; height: 34px; border-radius: 50%;
    background: var(--brand-blue);
  }
  .front-name {
    color: var(--text-white);
    font-size: 40px; font-weight: 400; letter-spacing: 0.5px;
  }
  .front-url {
    position: absolute; top: 170px; left: 0; right: 0;
    text-align: center;
    color: var(--text-white);
    font-size: 12px; font-weight: 600; letter-spacing: 0.5px;
  }

  .back-pattern {
    position: absolute; inset: 0;
    background: radial-gradient(ellipse at 55% 40%, var(--card-pattern-top), var(--card-pattern-bottom) 75%);
  }
  .back-brand {
    position: absolute; left: 40px; top: 128px;
    display: flex; align-items: center; gap: 10px;
  }
  .back-brand .brand-dot { width: 26px; height: 26px; }
  .back-name {
    color: var(--brand-blue);
    font-size: 25px; font-weight: 600;
  }
  .divider {
    position: absolute; left: 262px; top: 72px;
    width: 1px; height: 150px;
    background: var(--divider);
  }
  .contact {
    position: absolute; left: 280px; top: 86px;
  }
  .person-name {
    color: var(--brand-blue);
    font-size: 18px; font-weight: 600; letter-spacing: 0.5px;
    line-height: 1.1;
  }
  .person-title {
    color: var(--text-white);
    font-size: 14px; margin-bottom: 6px;
  }
  .contact-list { list-style: none; }
  .contact-list li {
    display: flex; align-items: center; gap: 8px;
    color: var(--text-soft);
    font-size: 14px; line-height: 22px;
  }
  .contact-list li.no-icon { padding-left: 20px; }
  .contact-list svg { width: 12px; height: 12px; fill: var(--brand-blue); flex: none; }
</style>
</head>
<body>

  <section class="card card-front" aria-label="Card front">
    <div class="front-brand">
      <span class="brand-dot"></span>
      <span class="front-name">Velnor Group</span>
    </div>
    <p class="front-url">www.velnorgroup.com</p>
  </section>

  <section class="card card-back" aria-label="Card back">
    <div class="back-pattern" role="img" aria-label="Faint repeating brand symbol pattern in dark blue"></div>
    <div class="back-brand">
      <span class="brand-dot"></span>
      <span class="back-name">Velnor Group</span>
    </div>
    <div class="divider"></div>
    <div class="contact">
      <p class="person-name">DANIEL REYES</p>
      <p class="person-title">CEO/FOUNDER</p>
      <ul class="contact-list">
        <li>
          <svg viewBox="0 0 24 24" aria-hidden="true"><path d="M6.6 10.8a15.1 15.1 0 0 0 6.6 6.6l2.2-2.2c.3-.3.7-.4 1-.2 1.1.4 2.3.6 3.6.6.6 0 1 .4 1 1V20c0 .6-.4 1-1 1A17 17 0 0 1 3 4c0-.6.4-1 1-1h3.5c.6 0 1 .4 1 1 0 1.3.2 2.5.6 3.6.1.3 0 .7-.2 1z"/></svg>
          555 210 4817
        </li>
        <li>
          <svg viewBox="0 0 24 24" aria-hidden="true"><path d="M7 1h10a2 2 0 0 1 2 2v18a2 2 0 0 1-2 2H7a2 2 0 0 1-2-2V3a2 2 0 0 1 2-2zm0 3v14h10V4zm5 15.5a1 1 0 1 0 0 2 1 1 0 0 0 0-2z"/></svg>
          555 382 6045
        </li>
        <li>
          <svg viewBox="0 0 24 24" aria-hidden="true"><path d="M2 5h20v14H2zm2 2v.5l8 5 8-5V7l-8 5z"/></svg>
          d.reyes@velnorgroup.com
        </li>
        <li>
          <svg viewBox="0 0 24 24" aria-hidden="true"><circle cx="12" cy="12" r="10"/></svg>
          www.velnorgroup.com
        </li>
      </ul>
    </div>
  </section>

</body>
</html>
```